Web Design Project

We are building a site on Wordpress that will sell signed posters from various popular music artists - the name of the site is The Harlow Lane Studio. Consumers will be able to select from a list of personal messages and once they purchase, receive a high quality unique poster from the artist with a rendered handwriting based on the artist agreement.
We don't want anything too complicated, but would prefer a modern clean aesthetic. This is an e-commerce site, and will include a basic shopping cart. The artist galleries will be straightforward and may include some branding in the artist's look and feel.
Some sites to consider: kelvo.com, brimwexhall.com, quorble.com - but we would like it a bit cleaner and less busy.
Reason: I will be accepting designs up until Sunday evening EST. Thank you!
Reason: Thank you for your submissions! The client is reviewing the submissions and needs to run this by management before we select.
Reason: We are still delayed on the client's end as they are doing some logo and color re-designs.
Thanks for your patience.
Reason: We are trying to confirm a design choice with the client. Apologies for the delay!

```html
<!DOCTYPE html>
<html lang="en">
<head>
<meta charset="utf-8">
<title>The Harlow Lane Studio</title>
<link rel="stylesheet" href="https://fonts.googleapis.com/css2?family=Cinzel&family=Open+Sans:wght@400;600;700&family=Quicksand:wght@300;400;500&display=swap">
<style>
:root{
  --bg-deep:#1c0c1a;
  --bg-mid:#2e1529;
  --plum:#4a2543;
  --plum-light:#6a3a60;
  --title:#8a3a7e;
  --text:#f4eef3;
  --muted:#cdb6c8;
  --accent:#e21bb4;
  --rule:#5a3a54;
}
*{margin:0;padding:0;box-sizing:border-box}
html,body{width:1200px;height:1018px;overflow:hidden}
body{
  position:relative;
  background:radial-gradient(ellipse at 50% 45%,#43203c 0%,var(--bg-mid) 45%,var(--bg-deep) 100%);
  font-family:"Open Sans",sans-serif;color:var(--text);
}
.abs{position:absolute}
.site-title{top:38px;left:0;width:1200px;text-align:center;font-family:"Cinzel",serif;font-size:39px;letter-spacing:3px;color:var(--title)}
.main-nav{top:124px;left:32px;width:1134px;height:52px;display:flex;justify-content:space-between;align-items:center;padding:0 38px 0 36px;
  background:linear-gradient(90deg,rgba(90,45,82,.2),rgba(110,58,100,.75) 50%,rgba(90,45,82,.2));
  font-family:"Quicksand",sans-serif;font-size:17px;color:#e8dce6}
.account-links{top:191px;right:43px;font-size:11px;font-weight:600;color:#fff}
.account-links span{margin:0 5px;font-weight:400}
.categories{top:227px;left:32px;width:233px}
.panel-head{height:37px;border-radius:5px;background:linear-gradient(#6b3b62,#4c2746);font-family:"Quicksand",sans-serif;font-size:18px;line-height:37px;padding-left:11px}
.categories ul{list-style:none;margin-top:4px}
.categories li{height:37.5px;line-height:37px;padding-left:24px;font-size:14px;border-bottom:1px solid var(--rule)}
.slide{border-radius:4px}
.slide-side-l{left:279px;top:281px;width:126px;height:228px;background:linear-gradient(135deg,#e8a432,#7a4410 55%,#2a1a18)}
.slide-side-r{left:808px;top:281px;width:113px;height:228px;background:linear-gradient(160deg,#c9a08a,#efe2dc 50%,#6b5048)}
.slide-main{left:405px;top:273px;width:403px;height:280px;background:linear-gradient(170deg,#3b2a30 0%,#b27a36 35%,#f0c470 50%,#5a3c2e 75%,#2a2230);box-shadow:0 0 18px rgba(0,0,0,.6)}
.reflect{left:279px;top:509px;width:642px;height:70px;background:linear-gradient(rgba(120,80,110,.35),rgba(0,0,0,0))}
.col-title{font-family:"Quicksand",sans-serif;font-size:18px;color:#e8dce6}
.col{top:577px}
.body-text{font-size:13.5px;line-height:20px;text-align:justify}
.body-text b{color:#1a0a16;font-weight:700}
.btn{height:24px;padding:0 12px;border-radius:5px;background:linear-gradient(#4d2746,#2a1226);box-shadow:0 1px 2px #000;font-size:11.5px;line-height:24px;color:var(--accent);text-align:center}
.vrule{top:574px;width:2px;height:281px;background:#6a4a64}
.date{color:var(--accent);font-weight:700;font-size:13.5px}
.learn{font-size:11.5px;color:var(--accent);text-align:right}
.search{left:933px;top:230px;width:233px;height:38px;border-radius:4px;background:var(--plum)}
.search .field{position:absolute;left:6px;top:7px;width:192px;height:24px;border-radius:4px;background:#1e0c1b}
.connect{left:933px;top:279px;width:233px;height:38px;border-radius:4px;background:var(--plum);font-family:"Quicksand",sans-serif;font-size:13px;line-height:38px;padding-left:7px}
.connect i{position:absolute;top:11px;width:18px;height:18px;border-radius:3px}
.newsletter{left:933px;top:339px;width:233px;height:74px;border-radius:6px;border:1px solid #6a4a64;background:linear-gradient(#3f1f39,#2c1428)}
.newsletter .field{position:absolute;left:10px;top:25px;width:213px;height:24px;border-radius:12px;background:#1a0a17;font-size:11px;line-height:24px;padding-left:13px}
.newsletter .go{position:absolute;right:3px;top:3px;width:30px;height:18px;border-radius:9px;background:#eee;color:#222;font-size:10px;font-weight:700;line-height:18px;text-align:center}
.signup{left:936px;top:413px;width:227px;height:27px;background:linear-gradient(#5a2e52,#3e1e39);font-size:14px;line-height:27px;padding-left:15px;font-weight:600}
.footer-band{top:906px;left:0;width:1200px;height:75px;background:linear-gradient(90deg,#3a1a35,#5a2e52 50%,#3a1a35)}
.footer-links{top:931px;left:32px;font-family:"Quicksand",sans-serif;font-size:12px;color:var(--muted)}
.footer-links span{margin:0 9px}
.copyright{top:981px;left:0;width:1200px;height:37px;background:#1a0a18;text-align:center;font-size:11px;line-height:37px}
</style>
</head>
<body>
<h1 class="abs site-title">THE HARLOW LANE STUDIO</h1>
<nav class="abs main-nav"><span>Home</span><span>Art Gallery</span><span>Signatures</span><span>Blog</span><span>Frames</span><span>Press</span><span>Contact</span></nav>
<div class="abs account-links">Your Account<span>|</span>View Basket (0)<span>|</span>Customer Service</div>

<aside class="abs categories">
  <div class="panel-head">Categories</div>
  <ul><li>Link 1</li><li>Link 2</li><li>Link 3</li><li>Link 4</li><li>Link 5</li><li>Link 6</li><li>Link 7</li></ul>
</aside>

<div class="abs reflect"></div>
<div class="abs slide slide-side-l" role="img" aria-label="Painting of a child on a dock at sunset"></div>
<div class="abs slide slide-side-r" role="img" aria-label="Painting of a girl in a white dress sitting on rocks"></div>
<div class="abs slide slide-main" role="img" aria-label="Painting of children fishing from a pier by a lighthouse at sunset"></div>

<section class="abs col" style="left:32px;width:267px">
  <h2 class="col-title" style="padding-left:11px">Artist SpotLight</h2>
  <div role="img" aria-label="Artist painting a colourful canvas" style="margin-top:14px;height:115px;background:linear-gradient(100deg,#8a5a40,#c99a80 40%,#5a4a8a 75%,#e8e0e4)"></div>
  <p class="body-text" style="margin-top:21px">Lorem Ipsum is simply dummy text of the printing and typesetting industry. Lorem Ipsum has been the industry's standard</p>
</section>
<div class="abs btn" style="left:114px;top:835px;width:92px">Learn more</div>
<div class="abs vrule" style="left:320px"></div>

<section class="abs col" style="left:340px;width:264px">
  <h2 class="col-title" style="padding-left:3px">News and Blog</h2>
  <p class="body-text" style="margin-top:26px"><b>Lorem Ipsum</b> is simply dummy text of the printing and typesetting industry. Lorem Ipsum .....</p>
  <div style="height:1px;background:var(--rule);margin:19px 0 18px"></div>
  <p class="body-text"><b>Lorem Ipsum</b> is simply dummy text of the printing and typesetting industry. Lorem Ipsum .....</p>
</section>
<div class="abs btn" style="left:433px;top:835px;width:90px">Learn more</div>
<div class="abs vrule" style="left:634px"></div>

<section class="abs col" style="left:658px;width:268px">
  <h2 class="col-title" style="padding-left:visible;margin-left:-3px">Upcoming Events</h2>
  <p class="body-text" style="margin-top:26px"><b>Lorem Ipsum</b> is simply dummy text of the printing and typesetting industry. Lorem Ipsum</p>
  <div class="date">10 Mar 2012</div>
  <div style="border-top:1px dashed #cbb;margin:9px 0 4px"></div>
  <p class="body-text"><b>Lorem Ipsum</b> is simply dummy text of the printing and typesetting industry. Lorem Ipsum</p>
  <div class="date">10 Mar 2012</div>
</section>
<div class="abs btn" style="left:749px;top:835px;width:90px">Learn more</div>

<div class="abs search"><div class="field"></div>
  <svg style="position:absolute;left:206px;top:9px" width="22" height="20" viewBox="0 0 22 20"><circle cx="8" cy="8" r="5.5" fill="none" stroke="#fff" stroke-width="2"/><line x1="12" y1="12" x2="20" y2="18" stroke="#fff" stroke-width="3" stroke-linecap="round"/></svg>
</div>
<div class="abs connect">Connect with Us
  <i style="left:122px;background:#8a6a84"></i><i style="left:147px;background:#7a8aa4"></i><i style="left:172px;background:#5a6e9a"></i><i style="left:197px;background:#c07a50"></i>
</div>
<div class="abs newsletter"><div class="field">enter your email id<span class="go">GO</span></div></div>
<div class="abs signup">Sign Up For Newsletter</div>
<div class="abs" role="img" aria-label="Pen writing a flourished signature" style="left:933px;top:456px;width:233px;height:113px;background:linear-gradient(120deg,#f8e8b8,#f2d08a 60%,#c89a5a)"></div>
<p class="abs body-text" style="left:939px;top:580px;width:225px">Lorem Ipsum is simply dummy text of the printing and typeset-ting industry.</p>
<div class="abs learn" style="left:933px;top:647px;width:233px">Learn more</div>
<div class="abs" style="left:933px;top:676px;width:233px;height:1px;background:var(--rule)"></div>
<div class="abs" style="left:936px;top:688px;width:22px;height:22px;border-radius:50%;background:#3a8ad0"></div>
<h2 class="abs col-title" style="left:964px;top:688px;font-size:17px">Chatter Feeds</h2>
<p class="abs" style="left:939px;top:720px;width:227px;font-size:12.5px;line-height:21px">Lorem Ipsum is simply dummy text of the printing .....</p>
<p class="abs" style="left:939px;top:777px;width:227px;font-size:12.5px;line-height:21px">Lorem Ipsum is simply dummy text of the printing .....</p>
<div class="abs learn" style="left:933px;top:836px;width:233px">Learn more</div>

<footer>
  <div class="abs footer-band"></div>
  <div class="abs footer-links">FAQ<span>|</span>Privacy Policy<span>|</span>Terms &amp; Conditions<span>|</span>Store Policy<span>|</span>Site Map</div>
  <div class="abs copyright">©2012 harlowlanestudio, All Rights Reserved</div>
</footer>
</body>
</html>
```